Glitch Tonic Energy Drink Website

We need a website to advertise and promote the product "Glitch Tonic". This is a product of https://www.bramblecrestco.net/glitchtonic.html but we want to move it to its own URL to promote the product. The theme needs to be extreme ports, gamer and cyber security orientated as these are our target audiences.

https://www.clipvista.example/shorts/Qp3Rt7WmZxA
https://www.clipvista.example/shorts/5Hdye2L-KNu

Target Market(s)

Extreme Sport, Online Gamers, Cyber Security Professionals

Coding

```html
<!DOCTYPE html>
<html lang="en">
<head>
<meta charset="utf-8">
<title>Glitch Tonic Energy</title>
<link href="https://fonts.googleapis.com/css2?family=Russo+One&family=Poppins:wght@400;500;600;700&display=swap" rel="stylesheet">
<style>
:root{
  --red:#b0121f;
  --red-deep:#8e0d18;
  --red-bright:#e0202e;
  --ink:#141414;
  --muted:#6b6b6b;
  --pink:#fbe3e5;
  --pink-soft:#fdf1f2;
  --white:#ffffff;
  --star:#f4b400;
}
*{box-sizing:border-box;margin:0;padding:0}
html,body{width:1200px;height:3544px;overflow:hidden}
body{font-family:"Poppins",sans-serif;color:var(--ink);background:var(--white);position:relative}
.display{font-family:"Russo One",sans-serif}
a{color:inherit;text-decoration:none}
.btn{display:inline-block;background:var(--red);color:var(--white);font-weight:600;font-size:14px;letter-spacing:.5px;padding:13px 30px;border-radius:3px}
.section-title{font-family:"Russo One",sans-serif;font-size:40px;letter-spacing:2px;text-align:center}
.title-bar{width:70px;height:5px;background:var(--red);margin:12px auto 0;border-radius:3px}

/* hero */
.hero{position:absolute;left:0;top:0;width:1200px;height:600px;background:linear-gradient(110deg,#2a0507 0%,#5e0a10 40%,#a3141d 70%,#5a0b10 100%);color:var(--white);overflow:hidden}
.hero-art{position:absolute;left:760px;top:50px;width:360px;height:550px;background:linear-gradient(180deg,#c9c4c4 0%,#6b2a2e 55%,#2a0a0c 100%);border-radius:160px 160px 0 0;opacity:.85}
.hero-scene{position:absolute;left:0;top:0;width:1200px;height:600px;background:radial-gradient(circle at 30% 75%,rgba(0,0,0,.45),transparent 45%)}
.nav{position:absolute;left:0;top:0;width:1200px;height:90px;display:flex;align-items:center;padding:0 110px}
.brand{font-family:"Russo One",sans-serif;line-height:1}
.brand .name{font-size:30px;display:block}
.brand .sub{font-size:13px;letter-spacing:1px}
.nav-links{display:flex;gap:34px;margin-left:auto;font-size:14px;font-weight:500;text-transform:uppercase}
.nav-links a.active{position:relative}
.nav-links a.active::after{content:"";position:absolute;left:50%;top:24px;width:9px;height:9px;margin-left:-4px;border-radius:50%;background:var(--white)}
.nav-icons{display:flex;gap:22px;margin-left:36px}
.hero-copy{position:absolute;left:110px;top:128px;width:460px}
.hero-copy .kicker{font-size:15px;font-weight:600;letter-spacing:1px}
.hero-copy h1{font-family:"Russo One",sans-serif;font-size:64px;line-height:1.05;margin:14px 0 20px}
.hero-copy h1 .accent{color:var(--red-bright)}
.hero-copy p{font-size:15px;line-height:1.6;margin-bottom:30px}
.hero-copy .btn{background:var(--red-bright)}

/* drink */
.drink{position:absolute;left:0;top:600px;width:1200px;height:672px;background:var(--white)}
.drink .section-title{padding-top:98px}
.drink-row{position:absolute;left:104px;top:200px;display:flex;gap:30px}
.product{width:317px;height:386px;background:var(--white);border-radius:8px;box-shadow:0 6px 22px rgba(0,0,0,.12);padding:14px;text-align:center}
.product-art{height:186px;border-radius:6px;background:linear-gradient(180deg,#ececec,#cfcfcf)}
.product h3{color:var(--red);font-size:19px;font-weight:700;margin-top:20px}
.product .flavour{font-size:13px;color:var(--muted);margin-top:4px}
.rating{display:flex;justify-content:center;align-items:center;gap:3px;margin-top:10px;font-size:13px;color:var(--muted)}
.rating span{margin-left:8px}
.product .price{color:var(--red);font-size:20px;font-weight:700;margin-top:14px}
.arrow{position:absolute;width:34px;height:34px;border-radius:50%;display:flex;align-items:center;justify-content:center}
.drink .arrow.prev{left:34px;top:378px;border:2px solid #9a9a9a}
.drink .arrow.next{left:1128px;top:378px;border:2px solid var(--red)}

/* about */
.about{position:absolute;left:0;top:1272px;width:1200px;height:448px;background:linear-gradient(180deg,var(--pink),#f6c9ce 60%,var(--pink));text-align:center;overflow:hidden}
.about-scene{position:absolute;left:0;top:0;width:1200px;height:448px;background:radial-gradient(ellipse at 50% 40%,rgba(255,255,255,.55),transparent 70%)}
.about-inner{position:relative;padding-top:64px}
.about .brand .name{font-size:30px;color:var(--ink)}
.about .brand .name .accent{color:var(--red)}
.about .brand .sub{color:var(--ink)}
.about .section-title{margin-top:24px}
.about p{width:960px;margin:26px auto 30px;font-size:14px;line-height:1.75;color:#333}

/* blogs */
.blogs{position:absolute;left:0;top:1720px;width:1200px;height:680px;background:var(--white);overflow:hidden}
.blogs .section-title{position:absolute;left:110px;top:152px;text-align:left}
.blogs .title-bar{position:absolute;left:110px;top:214px;margin:0}
.blogs .arrow.prev{left:976px;top:172px;color:#8a8a8a}
.blogs .arrow.next{left:1032px;top:170px;width:48px;height:36px;border:2px solid var(--red);border-radius:4px}
.blog-row{position:absolute;left:110px;top:270px;display:flex;gap:24px}
.post{width:372px;height:416px;background:var(--white);box-shadow:0 6px 22px rgba(0,0,0,.12);padding:10px}
.post-art{height:254px;background:linear-gradient(135deg,#1d2b3f,#4d5b70 55%,#8a6a4c)}
.post h3{font-size:19px;font-weight:700;line-height:1.4;margin:20px 10px 0}
.post-meta{display:flex;align-items:center;margin:16px 10px 0;font-size:12px;color:var(--muted)}
.post-meta svg{margin-right:10px}
.post-meta .btn{margin-left:auto;font-size:10px;padding:7px 14px}

/* events */
.events{position:absolute;left:0;top:2400px;width:1200px;height:744px;background:var(--pink-soft);overflow:hidden}
.events-texture{position:absolute;inset:0;background:radial-gradient(circle at 20% 30%,rgba(240,190,196,.35),transparent 40%),radial-gradient(circle at 80% 70%,rgba(240,190,196,.35),transparent 40%)}
.events .section-title{position:relative;padding-top:182px}
.event-row{position:absolute;left:100px;top:290px;display:flex;gap:36px}
.event{position:relative;width:312px;height:330px;background:var(--white);border-radius:10px;border-bottom:5px solid var(--red);box-shadow:0 6px 22px rgba(0,0,0,.12);overflow:visible}
.event-art{height:190px;border-radius:10px 10px 0 0;background:linear-gradient(135deg,#d9263a,#7a1434 55%,#2c1a4a)}
.event-date{position:absolute;right:18px;top:158px;width:66px;height:66px;border-radius:50%;background:var(--red);color:var(--white);text-align:center;border:4px solid var(--white);line-height:1}
.event-date b{display:block;font-size:22px;margin-top:12px}
.event-date small{font-size:11px;font-weight:600}
.event h3{font-size:20px;font-weight:700;margin:30px 20px 0}
.event p{font-size:13px;line-height:1.5;color:#444;margin:6px 20px 0}
.event .time{display:flex;align-items:center;gap:8px;font-size:12px;color:#444;margin:8px 20px 0}
.event-frame{position:absolute;left:-10px;top:-10px;width:332px;height:350px;border:3px solid var(--red);border-radius:12px;z-index:-1}
.events .btn{position:absolute;left:511px;top:676px;padding:15px 38px}

/* footer */
.footer{position:absolute;left:0;top:3144px;width:1200px;height:400px;background:var(--red);color:var(--white)}
.footer .brand{position:absolute;left:110px;top:100px}
.footer .brand .name{font-size:46px}
.footer .brand .sub{font-size:20px}
.contact{position:absolute;left:570px;top:118px;display:flex;align-items:center;gap:48px}
.mail{display:flex;align-items:center;gap:12px;font-size:16px}
.socials{display:flex;gap:12px}
.socials span{width:40px;height:40px;border-radius:50%;border:2px solid var(--white);display:block}
.foot-links{position:absolute;left:530px;top:202px;display:flex;gap:72px;font-size:14px;font-weight:500}
.foot-rule{position:absolute;left:110px;top:268px;width:980px;height:1px;background:rgba(255,255,255,.5)}
.copyright{position:absolute;left:0;top:300px;width:1200px;text-align:center;font-size:13px}
</style>
</head>
<body>

<header class="hero">
  <div class="hero-scene" role="img" aria-label="Dark red gaming room backdrop"></div>
  <div class="hero-art" role="img" aria-label="Illustrated gamer character holding an energy drink can"></div>
  <nav class="nav">
    <div class="brand"><span class="name">Glitch Tonic</span><span class="sub">ENERGY</span></div>
    <div class="nav-links">
      <a class="active" href="#">Home</a>
      <a href="#">About the brand</a>
      <a href="#">Services section</a>
      <a href="#">Contact details</a>
    </div>
    <div class="nav-icons">
      <svg width="20" height="20" viewBox="0 0 20 20" fill="none" stroke="#fff" stroke-width="2"><circle cx="8.5" cy="8.5" r="6.5"/><path d="M13.5 13.5L19 19"/></svg>
      <svg width="22" height="20" viewBox="0 0 22 20" fill="none" stroke="#fff" stroke-width="2"><path d="M1 2h4l3 11h10l3-8H7"/><circle cx="9" cy="17" r="1.5"/><circle cx="17" cy="17" r="1.5"/></svg>
    </div>
  </nav>
  <div class="hero-copy">
    <div class="kicker">WELCOME TO</div>
    <h1>GLITCH <span class="accent">TONIC</span><br>ENERGY</h1>
    <p>Lorem Ipsum is simply dummy text of the printing and typesetting industry. Lorem Ipsum has been the</p>
    <a class="btn" href="#">GET STARTED</a>
  </div>
</header>

<section class="drink">
  <h2 class="section-title">OUR DRINK</h2>
  <div class="title-bar"></div>
  <div class="arrow prev"><svg width="12" height="14" viewBox="0 0 12 14"><path d="M9 1L3 7l6 6" fill="none" stroke="#777" stroke-width="2.4"/></svg></div>
  <div class="drink-row">
    <article class="product">
      <div class="product-art" role="img" aria-label="Strawberry energy drink cans"></div>
      <h3>Glitch Tonic Energy</h3>
      <div class="flavour">Flavour : Strawberry</div>
      <div class="rating">
        <svg width="80" height="14" viewBox="0 0 80 14"><g fill="#f4b400"><path id="st" d="M7 0l2 4.6 5 .4-3.8 3.3 1.2 4.9L7 10.6 2.6 13.2l1.2-4.9L0 5l5-.4z"/><use href="#st" x="16"/><use href="#st" x="32"/><use href="#st" x="48"/></g><use href="#st" x="64" fill="#d8d8d8"/></svg>
        <span>1071 Reviews</span>
      </div>
      <div class="price">$25.00</div>
    </article>
    <article class="product">
      <div class="product-art" role="img" aria-label="Chocolate energy drink cans"></div>
      <h3>Glitch Tonic Energy</h3>
      <div class="flavour">Flavour : Chocolate</div>
      <div class="rating">
        <svg width="80" height="14" viewBox="0 0 80 14"><g fill="#f4b400"><use href="#st"/><use href="#st" x="16"/><use href="#st" x="32"/><use href="#st" x="48"/></g><use href="#st" x="64" fill="#d8d8d8"/></svg>
        <span>1071 Reviews</span>
      </div>
      <div class="price">$25.00</div>
    </article>
    <article class="product">
      <div class="product-art" role="img" aria-label="Butterscotch energy drink cans"></div>
      <h3>Glitch Tonic Energy</h3>
      <div class="flavour">Flavour : Butterscotch</div>
      <div class="rating">
        <svg width="80" height="14" viewBox="0 0 80 14"><g fill="#f4b400"><use href="#st"/><use href="#st" x="16"/><use href="#st" x="32"/><use href="#st" x="48"/></g><use href="#st" x="64" fill="#d8d8d8"/></svg>
        <span>1071 Reviews</span>
      </div>
      <div class="price">$25.00</div>
    </article>
  </div>
  <div class="arrow next"><svg width="12" height="14" viewBox="0 0 12 14"><path d="M3 1l6 6-6 6" fill="none" stroke="#b0121f" stroke-width="2.4"/></svg></div>
</section>

<section class="about">
  <div class="about-scene" role="img" aria-label="Faded gaming setup backdrop in pink tones"></div>
  <div class="about-inner">
    <div class="brand"><span class="name">GLITCH <span class="accent">TONIC</span></span><span class="sub">ENERGY</span></div>
    <h2 class="section-title">ABOUT OUR BRAND</h2>
    <div class="title-bar"></div>
    <p>The Bramblecrest Group of Companies is a specialist Security Solutions and Managed Services Provider who through the provision of our unique and specialised Information Security and Cyber Security Offerings, are able to meet the needs of our clients both locally and internationally. Our offerings cover the full spectrum of the Security realm, from the design and implementation of bespoke security solutions to the provision of comprehensive Managed Security Services.</p>
    <a class="btn" href="#">READ MORE</a>
  </div>
</section>

<section class="blogs">
  <h2 class="section-title">OUR BLOGS</h2>
  <div class="title-bar"></div>
  <div class="arrow prev"><svg width="22" height="14" viewBox="0 0 22 14"><path d="M21 7H2M8 1L2 7l6 6" fill="none" stroke="#888" stroke-width="2"/></svg></div>
  <div class="arrow next"><svg width="22" height="14" viewBox="0 0 22 14"><path d="M1 7h19M14 1l6 6-6 6" fill="none" stroke="#b0121f" stroke-width="2.2"/></svg></div>
  <div class="blog-row">
    <article class="post">
      <div class="post-art" role="img" aria-label="Gamer playing at a desk with an energy drink"></div>
      <h3>Lorem Ipsum is simply dummy text of the printing</h3>
      <div class="post-meta"><svg width="20" height="20" viewBox="0 0 20 20" fill="none" stroke="#b0121f" stroke-width="1.6"><rect x="2" y="4" width="16" height="14" rx="2"/><path d="M2 8h16M6 2v4M14 2v4"/></svg>February 11, 2024<a class="btn" href="#">READ MORE</a></div>
    </article>
    <article class="post">
      <div class="post-art" role="img" aria-label="Security analyst working at multiple monitors"></div>
      <h3>Lorem Ipsum is simply dummy text of the printing</h3>
      <div class="post-meta"><svg width="20" height="20" viewBox="0 0 20 20" fill="none" stroke="#b0121f" stroke-width="1.6"><rect x="2" y="4" width="16" height="14" rx="2"/><path d="M2 8h16M6 2v4M14 2v4"/></svg>February 11, 2024<a class="btn" href="#">READ MORE</a></div>
    </article>
    <article class="post">
      <div class="post-art" role="img" aria-label="Programmer coding at night with an energy drink"></div>
      <h3>Lorem Ipsum is simply dummy text of the printing</h3>
      <div class="post-meta"><svg width="20" height="20" viewBox="0 0 20 20" fill="none" stroke="#b0121f" stroke-width="1.6"><rect x="2" y="4" width="16" height="14" rx="2"/><path d="M2 8h16M6 2v4M14 2v4"/></svg>February 11, 2024<a class="btn" href="#">READ MORE</a></div>
    </article>
  </div>
</section>

<section class="events">
  <div class="events-texture" role="img" aria-label="Soft pink contour pattern background"></div>
  <h2 class="section-title">UPCOMING EVENTS</h2>
  <div class="title-bar" style="position:relative"></div>
  <div class="event-row">
    <article class="event">
      <div class="event-frame"></div>
      <div class="event-art" role="img" aria-label="Excited gamer at a gaming event"></div>
      <div class="event-date"><b>10</b><small>OCT</small></div>
      <h3>Lorem Ipsum</h3>
      <p>October 10 - simply dummy text of the printing and typesetting industry.</p>
      <div class="time"><svg width="16" height="16" viewBox="0 0 16 16" fill="none" stroke="#333" stroke-width="1.5"><circle cx="8" cy="8" r="6.5"/><path d="M8 4v4l3 2"/></svg>8:00 AM - 1:00 PM</div>
    </article>
    <article class="event">
      <div class="event-art" role="img" aria-label="Players celebrating at an esports tournament"></div>
      <div class="event-date"><b>13</b><small>OCT</small></div>
      <h3>Lorem Ipsum</h3>
      <p>October 13 - simply dummy text of the printing and typesetting industry.</p>
      <div class="time"><svg width="16" height="16" viewBox="0 0 16 16" fill="none" stroke="#333" stroke-width="1.5"><circle cx="8" cy="8" r="6.5"/><path d="M8 4v4l3 2"/></svg>8:00 AM - 1:00 PM</div>
    </article>
    <article class="event">
      <div class="event-art" role="img" aria-label="Gamer with headset in neon lighting"></div>
      <div class="event-date"><b>18</b><small>OCT</small></div>
      <h3>Lorem Ipsum</h3>
      <p>October 18 - simply dummy text of the printing and typesetting industry.</p>
      <div class="time"><svg width="16" height="16" viewBox="0 0 16 16" fill="none" stroke="#333" stroke-width="1.5"><circle cx="8" cy="8" r="6.5"/><path d="M8 4v4l3 2"/></svg>8:00 AM - 1:00 PM</div>
    </article>
  </div>
  <a class="btn" href="#">VIEW MORE</a>
</section>

<footer class="footer">
  <div class="brand"><span class="name">Glitch Tonic</span><span class="sub">ENERGY</span></div>
  <div class="contact">
    <div class="mail"><svg width="34" height="34" viewBox="0 0 34 34" fill="none" stroke="#fff" stroke-width="2"><circle cx="17" cy="17" r="16"/><rect x="9" y="11" width="16" height="12" rx="1.5"/><path d="M9 12l8 6 8-6"/></svg>info@glitchtonic.example</div>
    <div class="socials"><span></span><span></span><span></span><span></span></div>
  </div>
  <div class="foot-links">
    <a href="#">Home</a><a href="#">About The Brand</a><a href="#">Services Section</a><a href="#">Contact Details</a>
  </div>
  <div class="foot-rule"></div>
  <div class="copyright">© 2024 . Glitch Tonic Energy | All Rights Reserved</div>
</footer>

</body>
</html>
```